Kestro Vale - Dog Supplement Brand

Here a link to a word doc with all of my info.
Please read it carefully.
https://files.brindlepad.net/sheet/7QwLx2mTa8Rk3PzNv0eYc5Hj9UfGs46Bd1Oi-Lp-3/view?ref=shared
Its 2 pages. Home Page and Product Page.
Oh and btw: the poses I attached dont have a shadow, so it would be good if you added a shadow to the poses .
If you have any questions please let me know.
Target Market(s)
Dog Owners In UK
Industry/Entity Type
Dog supplements
Number of Pages Required
2 page
Requirements
Must have
- Home page and product page files. Super Hero Theme.

```html
<!DOCTYPE html>
<html lang="en">
<head>
<meta charset="utf-8">
<title>Kestro Vale – Home</title>
<link rel="stylesheet" href="https://fonts.googleapis.com/css2?family=Exo+2:ital,wght@0,600;0,800;1,700;1,800;1,900&family=Open+Sans:ital,wght@0,400;0,600;0,700;1,400&display=swap">
<style>
:root{
  --red:#e31b23;
  --red-deep:#b5121a;
  --hero-a:#c8341a;
  --hero-b:#6e1a0c;
  --yellow:#f5c518;
  --ink:#1d1d1f;
  --dark:#262628;
  --dark-2:#1c1c1e;
  --blob:#262a33;
  --text:#333;
  --muted:#777;
  --white:#fff;
  --line:#e4e4e4;
  --green-a:#6fb82a;
  --green-b:#2f7a12;
  --blue-a:#3aa0ef;
  --blue-b:#0b5fc4;
}
*{box-sizing:border-box;margin:0;padding:0}
html,body{width:1200px;height:4604px;overflow:hidden;background:var(--white)}
body{position:relative;font-family:"Open Sans",Arial,sans-serif;color:var(--text)}
.abs{position:absolute}
.display{font-family:"Exo 2",Arial,sans-serif;font-style:italic;font-weight:800}
.btn{position:absolute;display:flex;align-items:center;justify-content:center;background:var(--red);color:var(--white);font-family:"Exo 2",Arial,sans-serif;font-style:italic;font-weight:700;font-size:14px;border-radius:3px;box-shadow:3px 3px 0 var(--yellow)}
.center-x{left:0;width:1200px;text-align:center}

/* header */
.site-header{position:absolute;top:0;left:0;width:1200px;height:75px;background:var(--white)}
.menu-toggle{position:absolute;left:72px;top:28px;width:26px;height:18px;display:flex;flex-direction:column;justify-content:space-between}
.menu-toggle span{display:block;height:2px;background:var(--ink)}
.brand{position:absolute;left:0;width:1200px;top:22px;text-align:center;font-family:"Exo 2",Arial,sans-serif;font-weight:800;font-size:24px;color:var(--ink);letter-spacing:.5px}
.header-icons{position:absolute;right:70px;top:28px;display:flex;gap:18px}
.header-icons svg{width:18px;height:18px;stroke:var(--ink);fill:none;stroke-width:2}

/* hero */
.hero{position:absolute;top:75px;left:0;width:1200px;height:450px;background:radial-gradient(circle at 78% 40%,var(--hero-a) 0%,#a12612 45%,var(--hero-b) 100%)}
.hero-kicker{position:absolute;left:72px;top:130px;color:var(--white);font-size:17px}
.hero-title{position:absolute;left:70px;top:150px;font-size:60px;color:var(--white);line-height:1.1}
.hero-title em{font-style:inherit;color:var(--yellow)}
.hero-sub{position:absolute;left:72px;top:226px;color:var(--white);font-family:"Exo 2",Arial,sans-serif;font-style:italic;font-weight:700;font-size:20px}
.hero-jars{position:absolute;left:455px;top:225px;width:375px;height:225px;border-radius:18px 18px 4px 4px;background:linear-gradient(180deg,#f2f2f2,#cfd8c2 55%,#4caf3a)}
.hero-mascot{position:absolute;left:705px;top:105px;width:395px;height:455px;border-radius:45% 45% 40% 40%;background:linear-gradient(160deg,#f4f4f4 0%,#c9c9c9 45%,#2a2a2a 70%,#d9262a 100%);box-shadow:0 18px 28px rgba(0,0,0,.35)}

/* intro */
.intro-hi{top:555px;font-size:64px;color:var(--ink)}
.intro-title{top:625px;font-size:42px;color:var(--ink)}
.intro-copy{position:absolute;left:140px;top:703px;width:920px;text-align:center;font-size:16px;line-height:24px;color:var(--text)}

/* offers */
.offers{position:absolute;top:889px;left:0;width:1200px;height:1036px;background:linear-gradient(180deg,var(--dark) 0%,#2d2d2f 50%,var(--dark-2) 100%)}
.offers-title{position:absolute;top:70px;font-size:42px;color:var(--white)}
.offer{position:absolute;width:336px}
.offer svg{display:block;width:336px;height:297px}
.offer-name{margin-top:28px;text-align:center;font-family:"Exo 2",Arial,sans-serif;font-style:italic;font-weight:800;font-size:26px;color:var(--white);line-height:38px}

/* featured */
.featured-title{top:1965px;font-size:42px;color:var(--ink)}
.product{position:absolute;top:2053px;width:248px}
.product-frame{height:269px;border:1px solid var(--line);padding:18px 40px}
.product-jar{width:100%;height:100%;border-radius:16px 16px 6px 6px;background:linear-gradient(180deg,#f7f7f7 0%,#e6e6e6 25%,#7cc242 40%,#3e9b2b 85%,#e9e9e9 100%)}
.product-meta{text-align:center;margin-top:14px}
.product-tag{font-size:11px;color:var(--text)}
.product-name{font-family:"Exo 2",Arial,sans-serif;font-style:italic;font-weight:700;font-size:18px;color:var(--ink);margin-top:2px}
.product-price{font-size:13px;font-weight:700;color:var(--red);margin-top:6px}
.product-price s{font-weight:400;color:var(--muted);font-size:11px;margin-left:4px}

/* testimonials */
.reviews-band{position:absolute;top:2549px;left:0;width:1200px;height:446px;background:radial-gradient(circle at 40% 30%,#e23a3a 0%,var(--red) 40%,var(--red-deep) 100%)}
.reviews-title{top:2568px;font-size:44px;color:var(--white)}
.reviews-blob{position:absolute;left:270px;top:2740px;width:700px;height:560px}
.avatar{position:absolute;left:585px;top:2655px;width:142px;height:142px;border-radius:50%;border:5px solid var(--white);background:linear-gradient(160deg,#3a3a3a 0%,#7a6a5a 45%,#e8c9a8 100%)}
.reviewer{position:absolute;top:2820px;left:0;width:1310px;text-align:center;color:var(--white);font-size:26px}
.review-date{position:absolute;top:2858px;left:0;width:1310px;text-align:center;color:var(--white);font-size:13px}
.review-nav{position:absolute;left:835px;top:2913px;width:300px;display:flex;align-items:center;gap:6px;color:var(--white);font-size:13px;font-weight:700}
.review-nav i{flex:1;height:1px;background:var(--white)}
.review-text{position:absolute;left:295px;top:2972px;width:620px;text-align:center;color:var(--white);font-style:italic;font-size:14.5px;line-height:23px}
.quote-mark{position:absolute;left:570px;top:3090px;width:60px;font-family:Georgia,serif;font-size:90px;color:#555;line-height:1;text-align:center}
.reviews-mascot{position:absolute;left:70px;top:2780px;width:210px;height:420px;border-radius:46% 46% 30% 30%;background:linear-gradient(170deg,#f2f2f2 0%,#cfcfcf 40%,#2b2b2b 60%,#d9262a 90%);box-shadow:8px 16px 24px rgba(0,0,0,.25)}

/* vets */
.vets-title{top:3355px;font-size:42px;color:var(--ink)}
.vets-video{position:absolute;left:287px;top:3428px;width:626px;height:364px;background:linear-gradient(180deg,#c9d8e0 0%,#e9d3a4 40%,#7a8f98 62%,#c9b48e 80%,#8a7356 100%)}

/* why */
.why-title{top:3842px;font-size:42px;color:var(--ink)}
.why-card{position:absolute;top:3922px;width:336px;height:238px;border-radius:28px;display:flex;flex-direction:column;align-items:center;justify-content:center;color:var(--white);text-align:center;font-weight:700;font-size:21px;line-height:29px;box-shadow:0 6px 14px rgba(0,0,0,.2)}
.why-card svg{width:60px;height:60px;stroke:var(--white);fill:none;stroke-width:2.4;margin-bottom:14px}
.why-green{left:72px;background:radial-gradient(circle at 50% 35%,var(--green-a),var(--green-b))}
.why-red{left:432px;background:radial-gradient(circle at 50% 35%,#f04848,var(--red-deep))}
.why-blue{left:792px;background:radial-gradient(circle at 50% 35%,var(--blue-a),var(--blue-b))}

/* footer */
.site-footer{position:absolute;top:4215px;left:0;width:1200px;height:389px;background:var(--dark-2);color:#cfcfcf}
.foot-col{position:absolute;top:70px}
.foot-col h4{font-size:22px;font-weight:600;color:var(--white);margin-bottom:18px}
.foot-col a{display:block;font-size:13px;color:#cfcfcf;text-decoration:none;line-height:30px}
.newsletter-input{width:270px;height:38px;background:var(--white);color:#777;font-size:11px;padding:12px 16px}
.newsletter-btn{width:270px;height:36px;margin-top:6px;background:var(--red);color:var(--white);font-size:12px;font-weight:700;display:flex;align-items:center;justify-content:center}
.social{display:flex;gap:8px}
.social span{height:32px;padding:0 6px;background:#3a3a3c;color:var(--white);font-size:10px;display:flex;align-items:center}
.copyright{position:absolute;top:315px;left:0;width:1200px;text-align:center;font-size:12px;color:#cfcfcf}
.copyright em{font-style:normal;color:var(--red)}
.payments{position:absolute;right:70px;top:308px;display:flex;gap:4px}
.payments span{width:40px;height:24px;background:#e9e9e9;color:var(--ink);font-size:9px;font-weight:700;display:flex;align-items:center;justify-content:center;border-radius:2px}
</style>
</head>
<body>

<header class="site-header">
  <div class="menu-toggle"><span></span><span></span><span></span></div>
  <div class="brand">Kestro Vale</div>
  <div class="header-icons">
    <svg viewBox="0 0 20 20"><circle cx="8.5" cy="8.5" r="6"/><path d="M13 13l5 5"/></svg>
    <svg viewBox="0 0 20 20"><circle cx="10" cy="6.5" r="4"/><path d="M3 19c0-4 3-6.5 7-6.5s7 2.5 7 6.5"/></svg>
    <svg viewBox="0 0 20 20"><path d="M4 7h12l-1 11H5z"/><path d="M7 7V5a3 3 0 016 0v2"/></svg>
  </div>
</header>

<section class="hero">
  <p class="hero-kicker">Join Forces With</p>
  <h1 class="hero-title display">Kestro <em>Vale</em></h1>
  <p class="hero-sub">&amp; Let Him Be Your Beloved Dog's Hero!</p>
  <a class="btn" style="left:72px;top:275px;width:140px;height:38px">Join Forces</a>
  <div class="hero-jars" role="img" aria-label="Three Kestro Vale multivitamin jars"></div>
</section>
<div class="hero-mascot" role="img" aria-label="Superhero husky mascot in a red cape"></div>

<section>
  <h2 class="abs center-x display intro-hi">Hi!</h2>
  <h2 class="abs center-x display intro-title">I am Kestro Vale</h2>
  <p class="intro-copy">Lorem ipsum dolor sit amet, consectetur adipisicing elit, sed do eiusmod tempor incididunt ut labore et dolore magna aliqua. Ut enim ad minim veniam, quis nostrud exercitation ullamco laboris nisi ut aliquip ex ea commodo consequat...</p>
  <a class="btn" style="left:530px;top:805px;width:140px;height:35px">Read More</a>
</section>

<section class="offers">
  <h2 class="abs center-x display offers-title">Here's What I Offer</h2>
  <svg width="0" height="0" style="position:absolute">
    <defs>
      <path id="shield" d="M168 2C196 30 250 36 296 14L336 62C336 150 336 200 300 250C270 286 220 276 168 297C116 276 66 286 36 250C0 200 0 150 0 62L40 14C86 36 140 30 168 2Z"/>
    </defs>
  </svg>
  <div class="offer" style="left:72px;top:160px">
    <svg viewBox="0 0 336 297" role="img" aria-label="Pug in a knitted scarf on yellow"><defs><linearGradient id="g1" x1="0" y1="0" x2="0" y2="1"><stop offset="0" stop-color="#f0b90f"/><stop offset="1" stop-color="#3a3a3a"/></linearGradient></defs><use href="#shield" fill="url(#g1)"/></svg>
    <p class="offer-name">Kestro Vale Calm</p>
  </div>
  <div class="offer" style="left:432px;top:160px">
    <svg viewBox="0 0 336 297" role="img" aria-label="Brown retriever by the sea"><defs><linearGradient id="g2" x1="0" y1="0" x2="0" y2="1"><stop offset="0" stop-color="#d7e6ec"/><stop offset=".5" stop-color="#a5542a"/><stop offset="1" stop-color="#2f7f9a"/></linearGradient></defs><use href="#shield" fill="url(#g2)"/></svg>
    <p class="offer-name">Kestro Vale Joint Support</p>
  </div>
  <div class="offer" style="left:792px;top:160px">
    <svg viewBox="0 0 336 297" role="img" aria-label="Golden retriever carrying a stick"><defs><linearGradient id="g3" x1="0" y1="0" x2="0" y2="1"><stop offset="0" stop-color="#bcd4dc"/><stop offset=".5" stop-color="#d9a868"/><stop offset="1" stop-color="#b07a40"/></linearGradient></defs><use href="#shield" fill="url(#g3)"/></svg>
    <p class="offer-name">Kestro Vale MultiVits</p>
  </div>
  <div class="offer" style="left:72px;top:561px">
    <svg viewBox="0 0 336 297" role="img" aria-label="Black and white spotted terrier"><defs><linearGradient id="g4" x1="0" y1="0" x2="0" y2="1"><stop offset="0" stop-color="#7f8a86"/><stop offset=".5" stop-color="#e6e6e6"/><stop offset="1" stop-color="#4d5a52"/></linearGradient></defs><use href="#shield" fill="url(#g4)"/></svg>
    <p class="offer-name">Kestro Vale Omega 369</p>
  </div>
  <div class="offer" style="left:432px;top:561px">
    <svg viewBox="0 0 336 297" role="img" aria-label="Tricolour terrier on a pink background"><defs><linearGradient id="g5" x1="0" y1="0" x2="0" y2="1"><stop offset="0" stop-color="#ecd7cc"/><stop offset=".5" stop-color="#3b2a22"/><stop offset="1" stop-color="#c08452"/></linearGradient></defs><use href="#shield" fill="url(#g5)"/></svg>
    <p class="offer-name">Kestro Vale Probiotics</p>
  </div>
  <div class="offer" style="left:792px;top:561px">
    <svg viewBox="0 0 336 297" role="img" aria-label="Smiling beagle"><defs><linearGradient id="g6" x1="0" y1="0" x2="0" y2="1"><stop offset="0" stop-color="#e3d6c8"/><stop offset=".5" stop-color="#c78a4a"/><stop offset="1" stop-color="#f1ede8"/></linearGradient></defs><use href="#shield" fill="url(#g6)"/></svg>
    <p class="offer-name">Kestro Vale Digestive<br>Support</p>
  </div>
</section>

<section>
  <h2 class="abs center-x display featured-title">Featured Products</h2>
  <div class="product" style="left:71px">
    <div class="product-frame"><div class="product-jar" role="img" aria-label="Multivitamin jar"></div></div>
    <div class="product-meta"><p class="product-tag">Hushpaw Trial</p><p class="product-name">Deliver Every 30 Days</p><p class="product-price">£10.00 GBP<s>£39.95 GBP</s></p></div>
  </div>
  <div class="product" style="left:341px">
    <div class="product-frame"><div class="product-jar" role="img" aria-label="Joint support powder tub"></div></div>
    <div class="product-meta"><p class="product-tag">Kestro Vale</p><p class="product-name">Joint Support - 150g Powder</p><p class="product-price">£24.00 GBP<s>£29.95 GBP</s></p></div>
  </div>
  <div class="product" style="left:611px">
    <div class="product-frame"><div class="product-jar" role="img" aria-label="Multivitamin jar"></div></div>
    <div class="product-meta"><p class="product-tag">Hushpaw Trial</p><p class="product-name">Deliver Every 120 Days</p><p class="product-price">£10.00 GBP<s>£39.95 GBP</s></p></div>
  </div>
  <div class="product" style="left:881px">
    <div class="product-frame"><div class="product-jar" role="img" aria-label="Multivitamin jar"></div></div>
    <div class="product-meta"><p class="product-tag">Hushpaw Trial</p><p class="product-name">Deliver Every 30 Days</p><p class="product-price">£10.00 GBP<s>£39.95 GBP</s></p></div>
  </div>
  <a class="btn" style="left:517px;top:2455px;width:164px;height:35px">View all Products</a>
</section>

<section>
  <div class="reviews-band" role="img" aria-label="Red toned photo of a spaniel"></div>
  <h2 class="abs center-x display reviews-title">People Love Me</h2>
  <div class="reviews-mascot" role="img" aria-label="Husky mascot sitting in a red cape"></div>
  <svg class="reviews-blob" viewBox="0 0 700 560" aria-hidden="true">
    <path fill="var(--blob)" d="M205 40C265 0 425 10 485 30C545 50 545 120 565 160C605 200 700 200 700 270C700 340 610 352 525 362C445 372 445 440 425 500C405 560 305 572 265 540C225 508 245 440 175 405C105 378 0 360 0 282C0 215 90 200 140 180C185 160 165 80 205 40Z"/>
  </svg>
  <div class="avatar" role="img" aria-label="Reviewer portrait"></div>
  <p class="reviewer">Mara Penhold</p>
  <p class="review-date">January 11, 2022</p>
  <div class="review-nav"><i></i><span>PREV | NEXT</span></div>
  <p class="review-text">Sed ut perspiciatis unde omnis iste natus error sit voluptatem accusantium doloremque laudantium, totam rem aperiam, eaque ipsa quae ab illo inventore veritatis et quasi architecto beatae vitae dicta sunt explicabo. &nbsp;Nemo enim ipsam voluptatem quia voluptas sit aspernatur aut odit aut fugit, sed quia consequuntur magni</p>
  <div class="quote-mark">”</div>
</section>

<section>
  <h2 class="abs center-x display vets-title">Approved By Expert Vets</h2>
  <div class="vets-video" role="img" aria-label="Video of a dog on a beach at sunset"></div>
</section>

<section>
  <h2 class="abs center-x display why-title">Why Choose Us</h2>
  <div class="why-card why-green">
    <svg viewBox="0 0 60 60"><circle cx="30" cy="30" r="26"/><path d="M30 14v32M22 22l8 6 8-6M22 32l8 6 8-6"/></svg>
    <p>Only Organic &amp; Natural<br>Ingredients</p>
  </div>
  <div class="why-card why-red">
    <svg viewBox="0 0 60 60"><path d="M14 18l8-8 12 4 12 8-2 12-10 6-8 14-10-4 2-14-8-10z"/><circle cx="32" cy="24" r="2"/></svg>
    <p>20% off for all Kestro Vale<br>Squad members</p>
  </div>
  <div class="why-card why-blue">
    <svg viewBox="0 0 60 60"><path d="M6 16h30v24H6zM36 24h10l8 8v8H36z"/><circle cx="16" cy="44" r="4"/><circle cx="44" cy="44" r="4"/><path d="M2 24h12M2 30h10"/></svg>
    <p>Free next Day UK<br>Delivery</p>
  </div>
</section>

<footer class="site-footer">
  <div class="foot-col" style="left:70px">
    <h4>Quick Links</h4>
    <a>Join Kestro Vale!</a><a>Browse Supplements</a><a>About Kestro Vale</a><a>Reviews</a><a>Need Help?</a><a>Legal</a>
  </div>
  <div class="foot-col" style="left:376px">
    <h4>Other Link</h4>
    <a>Privacy Policy</a><a>My Account</a><a>My cart</a><a>Search</a><a>Terms &amp; Conditions</a>
  </div>
  <div class="foot-col" style="left:640px">
    <h4>Newsletter</h4>
    <div class="newsletter-input">Enter Your Email:</div>
    <div class="newsletter-btn">SUBSCRIBE</div>
  </div>
  <div class="foot-col" style="left:980px">
    <h4 style="text-align:right;width:136px">Follow Us</h4>
    <div class="social"><span>Yappr</span><span>Barkly</span><span>Snoutly</span></div>
  </div>
  <p class="copyright">Copyright © 2022 <em>Kestro Vale</em>. All Rights Reserved.</p>
  <div class="payments"><span>Orbpay</span><span>Tallo</span><span>Nimcard</span><span>Quell</span></div>
</footer>

</body>
</html>
```